Brightwell Pictures Business Card

Hello,

i would like to have a dynamic, creative but tasteful card, colour used, front and back. I have attached a sample card that I liked very much from another individual to give you an idea of the theme/approach, but not colour. Ideally the graphic elements of the Brightwell Logo are brought into the design.

Target Market(s)

North America

Industry/Entity Type

Film Production

Contact Information for Business Card

Mirela Vantasch
President/Founder
Brightwell Pictures Inc.
587 914 3362
mirela@brightwellpix.tv

Font styles to use
Sans Serif

Colors
6b449b
5c5c5c
fdfdfd
000000

Requirements
Must have
• Logo, name, Company name, email and cell number. no Address line to be included.
Should not have
• any unrelated GFX elements, serif fonts

```html
<!DOCTYPE html>
<html lang="en">
<head>
<meta charset="utf-8">
<title>Brightwell Pictures Business Card</title>
<link href="https://fonts.googleapis.com/css2?family=Bebas+Neue&family=Questrial&display=swap" rel="stylesheet">
<style>
  :root {
    --brand-purple: #6b449b;
    --brand-purple-deep: #5a3888;
    --brand-grey: #5c5c5c;
    --paper: #fdfdfd;
    --ink: #000000;
    --dash-dark: #2b2b2b;
    --stage: #ecebef;
  }
  * { margin: 0; padding: 0; box-sizing: border-box; }
  html, body { width: 1200px; height: 1000px; overflow: hidden; }
  body {
    background: var(--stage);
    position: relative;
    font-family: "Questrial", "Century Gothic", sans-serif;
  }
  .card {
    position: absolute;
    width: 520px;
    height: 300px;
    border-radius: 18px;
    background: var(--paper);
    overflow: hidden;
    box-shadow: 0 6px 18px rgba(0,0,0,0.18);
  }
  .card--front { left: 50px; top: 350px; }
  .card--back  { left: 630px; top: 350px; }

  .front-logo {
    position: absolute;
    left: 0; right: 0; top: 0; bottom: 0;
    display: flex;
    align-items: center;
    justify-content: center;
    gap: 16px;
  }
  .front-logo__mark {
    width: 44px; height: 44px;
    border-radius: 50%;
    background: var(--brand-purple);
  }
  .front-logo__name {
    font-family: "Bebas Neue", "Oswald", sans-serif;
    font-size: 58px;
    letter-spacing: 1px;
    color: var(--brand-grey);
  }

  .back-art { position: absolute; inset: 0; }

  .holder { position: absolute; left: 28px; top: 26px; }
  .holder__name {
    font-family: "Bebas Neue", "Oswald", sans-serif;
    font-size: 34px;
    line-height: 1;
    letter-spacing: 1px;
    color: var(--brand-purple);
  }
  .holder__title {
    font-size: 13px;
    color: var(--ink);
    margin-top: 2px;
  }

  .contact {
    position: absolute;
    right: 26px;
    top: 196px;
    text-align: right;
    color: var(--paper);
  }
  .contact__company {
    font-family: "Bebas Neue", "Oswald", sans-serif;
    font-size: 27px;
    line-height: 1;
    letter-spacing: 1px;
  }
  .contact__line {
    font-size: 16px;
    line-height: 1.3;
  }
  .contact__phone { margin-top: 6px; }
</style>
</head>
<body>

  <section class="card card--front" aria-label="Card front">
    <div class="front-logo">
      <span class="front-logo__mark"></span>
      <span class="front-logo__name">Brightwell Pictures</span>
    </div>
  </section>

  <section class="card card--back" aria-label="Card back">
    <svg class="back-art" viewBox="0 0 520 300" width="520" height="300" aria-hidden="true">
      <defs>
        <linearGradient id="bandGradient" x1="0" y1="0" x2="1" y2="1">
          <stop offset="0" stop-color="#7a53ab"/>
          <stop offset="1" stop-color="#5e3a8e"/>
        </linearGradient>
      </defs>
      <!-- upper dashed path -->
      <path d="M0 68 C 120 110, 280 150, 405 128" fill="none"
            stroke="var(--dash-dark)" stroke-width="5" stroke-dasharray="10 7"/>
      <path d="M0 68 C 120 110, 280 150, 405 128" fill="none"
            stroke="var(--brand-purple)" stroke-width="5" stroke-dasharray="10 41" stroke-dashoffset="-17"/>
      <!-- lower purple band -->
      <path d="M0 225 C 120 165, 320 150, 520 190 L520 300 L0 300 Z" fill="url(#bandGradient)"/>
      <path d="M0 225 C 120 165, 320 150, 520 190" fill="none"
            stroke="var(--dash-dark)" stroke-width="5" stroke-dasharray="10 7"/>
      <!-- plain circle mark -->
      <circle cx="458" cy="112" r="46" fill="var(--brand-purple)"/>
    </svg>

    <div class="holder">
      <p class="holder__name">Mirela Vantasch</p>
      <p class="holder__title">President/Founder</p>
    </div>

    <div class="contact">
      <p class="contact__company">Brightwell Pictures Inc.</p>
      <p class="contact__line contact__phone">587 914 3362</p>
      <p class="contact__line">mirela@brightwellpix.tv</p>
    </div>
  </section>

</body>
</html>
```